I need a business card.

I need a simple, minimalist, business card. I think the coolest business card I have ever seen is Marty Vexler's from Brimstone Heist... it is just a little creepy for the real world.
I am a photographer and I need a card that I can give to brides or potential portrait customers that is simple and classy.
My name is Gil Anstrade. My website is www.gilanstrade-example.com
Please design my card.
I think it could be as simple as my name, phone # and website... where the rest of my contact could be found... or maybe my email and no website... I am open to ideas. I imagined the card on thick card stock with a black background...

```html
<!DOCTYPE html>
<html lang="en">
<head>
<meta charset="utf-8">
<title>Gil Anstrade Business Card</title>
<link href="https://fonts.googleapis.com/css2?family=Comfortaa:wght@300;400;600&family=Tinos&display=swap" rel="stylesheet">
<style>
  :root {
    --page-bg: #e3e3e3;
    --card-black: #030303;
    --band-outer: #2b2b2b;
    --band-inner: #161616;
    --frame-line: #5a5a5a;
    --ornament-fill: #8a8a8a;
    --text-white: #f2f2f2;
    --text-silver: #d8d8d8;
    --silver-top: #f4f4f4;
    --silver-bottom: #7a7a7a;
  }
  * { margin: 0; padding: 0; box-sizing: border-box; }
  html, body {
    width: 1200px;
    height: 873px;
    overflow: hidden;
    background: var(--page-bg);
  }
  .canvas {
    position: relative;
    width: 1200px;
    height: 873px;
  }
  .card {
    position: absolute;
    left: 265px;
    width: 680px;
    height: 387px;
    background: var(--card-black);
    box-shadow: 2px 3px 6px rgba(0,0,0,0.35);
    overflow: hidden;
  }
  .card--front { top: 41px; }
  .card--back { top: 451px; }
  .card-art {
    position: absolute;
    inset: 0;
    width: 680px;
    height: 387px;
  }
  .corner-ornament {
    position: absolute;
    width: 22px;
    height: 22px;
    background: linear-gradient(135deg, var(--ornament-fill), #3a3a3a);
    opacity: 0.8;
  }
  .corner-ornament--left { left: 22px; top: 340px; }
  .corner-ornament--right { left: 636px; top: 340px; }

  .card-name {
    position: absolute;
    top: 188px;
    left: 0;
    width: 100%;
    text-align: center;
    font-family: "Comfortaa", sans-serif;
    font-weight: 400;
    font-size: 50px;
    letter-spacing: -1px;
    word-spacing: 14px;
    line-height: 1;
  }
  .card-name__text {
    display: inline-block;
    background: linear-gradient(180deg, var(--silver-top) 10%, var(--silver-bottom) 95%);
    -webkit-background-clip: text;
    background-clip: text;
    color: transparent;
  }
  .card-name__reflection {
    display: block;
    transform: scaleY(-1);
    margin-top: -6px;
    background: linear-gradient(0deg, rgba(200,200,200,0.35) 0%, rgba(200,200,200,0) 55%);
    -webkit-background-clip: text;
    background-clip: text;
    color: transparent;
  }

  .contact-block {
    position: absolute;
    top: 184px;
    text-align: center;
    width: 300px;
  }
  .contact-block--phone { left: 21px; }
  .contact-block--web { left: 357px; }
  .contact-label {
    font-family: "Comfortaa", sans-serif;
    font-weight: 600;
    font-size: 24px;
    color: var(--text-white);
    word-spacing: 6px;
    letter-spacing: 0.5px;
  }
  .contact-value {
    margin-top: 18px;
    font-family: "Tinos", serif;
    font-size: 22px;
    color: var(--text-silver);
    letter-spacing: 0.5px;
  }
  .contact-block--web .contact-value { font-size: 20px; }
</style>
</head>
<body>
<div class="canvas">

  <section class="card card--front">
    <svg class="card-art" viewBox="0 0 680 387" aria-hidden="true">
      <path d="M0,0 H680 V0 C650,40 600,62 520,72 C420,84 300,82 200,108 C110,130 40,150 0,178 Z" fill="var(--band-outer)"/>
      <path d="M0,0 H650 C620,35 570,52 500,60 C400,70 290,68 190,94 C110,114 45,136 0,160 Z" fill="var(--band-inner)"/>
      <line x1="26" y1="165" x2="26" y2="362" stroke="var(--frame-line)" stroke-width="1"/>
      <line x1="654" y1="55" x2="654" y2="362" stroke="var(--frame-line)" stroke-width="1"/>
      <line x1="26" y1="362" x2="654" y2="362" stroke="var(--frame-line)" stroke-width="1"/>
    </svg>
    <div class="corner-ornament corner-ornament--left" role="img" aria-label="Silver filigree corner ornament"></div>
    <div class="corner-ornament corner-ornament--right" role="img" aria-label="Silver filigree corner ornament"></div>
    <h1 class="card-name">
      <span class="card-name__text">gil anstrade</span>
      <span class="card-name__reflection" aria-hidden="true">gil anstrade</span>
    </h1>
  </section>

  <section class="card card--back">
    <svg class="card-art" viewBox="0 0 680 387" aria-hidden="true">
      <path d="M0,0 H680 V0 C650,40 600,62 520,72 C420,84 300,82 200,108 C110,130 40,150 0,178 Z" fill="var(--band-outer)"/>
      <path d="M0,0 H650 C620,35 570,52 500,60 C400,70 290,68 190,94 C110,114 45,136 0,160 Z" fill="var(--band-inner)"/>
      <line x1="26" y1="165" x2="26" y2="362" stroke="var(--frame-line)" stroke-width="1"/>
      <line x1="654" y1="55" x2="654" y2="362" stroke="var(--frame-line)" stroke-width="1"/>
      <line x1="26" y1="362" x2="654" y2="362" stroke="var(--frame-line)" stroke-width="1"/>
    </svg>
    <div class="corner-ornament corner-ornament--left" role="img" aria-label="Silver filigree corner ornament"></div>
    <div class="corner-ornament corner-ornament--right" role="img" aria-label="Silver filigree corner ornament"></div>
    <div class="contact-block contact-block--phone">
      <p class="contact-label">phone number</p>
      <p class="contact-value">555.014.2870</p>
    </div>
    <div class="contact-block contact-block--web">
      <p class="contact-label">website</p>
      <p class="contact-value">www.gilanstrade-example.com</p>
    </div>
  </section>

</div>
</body>
</html>
```